Wellmere Talking Therapies House

We need a design for magazine advert, ideally high resolution to advertise our counselling centre. we would like this to include a photo of two people talking, as if in a counselling session. See our logo and colour range on our website. www.wellmere-house.co.uk
The photo should not include cups of coffee, clipboards, desks, people touching. it needs to be two people in armchairs sympathetically listening and looking at each other.
The font type is Great Vibes on the logo. Our design should communicate a centre of excellence delivering high quality, professional services in stylishly furnished surroundings.
Updates

Hello Everyone We have had a number of designs that look quite promising but are missing the brief. Can I reiterate that we need a photograph of 2 people seated talking to each other in a sincere way. There shouldn't be office chairs but comfortable chairs. There should be no physical contact. There should be no clipboards.Thank you very muchHeather Added Sunday, March 12, 2017

Target Market(s)

people seeking counselling and psychotherapy

Font styles to use
Other font styles liked:
• Great Vibes as in our logo for some of the print. See attached file.

Requirements
Must have
• good photograph
• Two high res Pixelvane photos:
• https://pixelvane-files.example-portal.net/download/photo-one-ref-7341
• https://pixelvane-files.example-portal.net/download/photo-two-ref-9826
Nice to have
• Watermark in keeping with our logo.
Should not have
• Darkness

```html
<!DOCTYPE html>
<html lang="en">
<head>
<meta charset="utf-8">
<title>Wellmere Talking Therapies House – Magazine Advert</title>
<link rel="stylesheet" href="https://fonts.googleapis.com/css2?family=Great+Vibes&family=Montserrat:wght@400;500;700&display=swap">
<style>
  :root {
    --page-bg: #e7e5df;
    --paper: #ffffff;
    --cream: #f3ecdd;
    --sage: #7d9f6e;
    --sage-light: #a8bd8a;
    --sage-text: #a9c08c;
    --espresso: #3d3433;
    --ink: #3a2e2d;
    --white: #ffffff;
  }
  html, body {
    margin: 0;
    padding: 0;
    width: 1200px;
    height: 1200px;
    overflow: hidden;
    background: var(--page-bg);
  }
  .canvas {
    position: relative;
    width: 1200px;
    height: 1200px;
  }
  .advert {
    position: absolute;
    left: 175px;
    top: 0;
    width: 969px;
    height: 1368px;
    transform: scale(0.877);
    transform-origin: top left;
    background: var(--paper);
    overflow: hidden;
    font-family: "Montserrat", sans-serif;
  }
  .advert__backdrop {
    position: absolute;
    inset: 0;
  }
  .headline {
    position: absolute;
    left: 98px;
    top: 40px;
    margin: 0;
    font-family: "Great Vibes", cursive;
    font-weight: 400;
    font-size: 70px;
    line-height: 72px;
    color: var(--ink);
  }
  .quote {
    position: absolute;
    left: 137px;
    top: 246px;
    width: 340px;
    margin: 0;
    color: var(--white);
    font-size: 17px;
    line-height: 24.5px;
    font-weight: 500;
  }
  .quote__author {
    display: block;
    text-align: right;
    margin-top: 4px;
  }
  .therapists {
    position: absolute;
    left: 137px;
    top: 1100px;
    width: 360px;
    color: var(--white);
  }
  .therapists__lead {
    margin: 0 0 2px;
    font-family: "Great Vibes", cursive;
    font-size: 72px;
    line-height: 76px;
    font-weight: 400;
  }
  .therapists__body {
    margin: 0;
    font-size: 19px;
    line-height: 28px;
    font-weight: 500;
  }
  .therapists__highlight {
    display: block;
    color: var(--sage-text);
    font-weight: 700;
  }
  .brand {
    position: absolute;
    left: 548px;
    top: 896px;
    width: 360px;
    text-align: center;
  }
  .brand__dot {
    display: block;
    width: 58px;
    height: 58px;
    margin: 0 auto 22px;
    border-radius: 50%;
    background: var(--sage);
  }
  .brand__name {
    margin: 0;
    font-size: 24px;
    line-height: 30px;
    font-weight: 500;
    color: var(--espresso);
  }
  .contact {
    position: absolute;
    left: 578px;
    top: 1112px;
    width: 340px;
    color: var(--espresso);
  }
  .contact__hours {
    margin: 0 0 14px;
    font-size: 19px;
    line-height: 24px;
    font-weight: 500;
  }
  .contact__row {
    display: flex;
    align-items: center;
    gap: 22px;
    margin-bottom: 10px;
  }
  .contact__icon {
    flex: 0 0 26px;
    width: 26px;
    height: 26px;
  }
  .contact__phone {
    font-size: 38px;
    line-height: 44px;
    font-weight: 500;
    letter-spacing: 0.5px;
  }
  .contact__text {
    font-size: 17px;
    line-height: 21px;
    font-weight: 500;
  }
</style>
</head>
<body>
<div class="canvas">
  <article class="advert">
    <svg class="advert__backdrop" width="969" height="1368" viewBox="0 0 969 1368" aria-hidden="false">
      <defs>
        <linearGradient id="photoTone" x1="0" y1="0" x2="1" y2="1">
          <stop offset="0" stop-color="#eef0ef"/>
          <stop offset="0.45" stop-color="#d9e4e0"/>
          <stop offset="0.75" stop-color="#e8d9d3"/>
          <stop offset="1" stop-color="#cfc9c2"/>
        </linearGradient>
        <radialGradient id="leafTone" cx="0.5" cy="0.55" r="0.55">
          <stop offset="0" stop-color="#d3dcc3"/>
          <stop offset="1" stop-color="#ffffff" stop-opacity="0"/>
        </radialGradient>
      </defs>
      <!-- cream diagonal field -->
      <polygon class="cream-field" points="969,283 969,1368 0,1368 0,903" fill="var(--cream)"/>
      <!-- quote panel -->
      <path class="quote-panel" d="M98,244 a26,26 0 0 1 26,-26 h363 a26,26 0 0 1 26,26 V980 H98 Z" fill="var(--sage)"/>
      <!-- therapists panel -->
      <rect class="therapists-panel" x="98" y="963" width="415" height="405" fill="var(--espresso)"/>
      <!-- leaf decoration area -->
      <ellipse class="leaf-spray" cx="745" cy="245" rx="170" ry="88" fill="url(#leafTone)" role="img" aria-label="Spray of soft sage leaves"/>
      <!-- leaf-shaped photo frame -->
      <path class="session-photo" d="M918,318 C700,330 430,380 250,520 C60,670 20,900 110,1000 C200,1080 420,1050 560,920 C740,760 880,520 918,318 Z"
            fill="url(#photoTone)" stroke="var(--sage-light)" stroke-width="14" stroke-linejoin="round"
            role="img" aria-label="Photograph of two women seated in comfortable chairs in a bright, calm counselling room"/>
    </svg>

    <h1 class="headline">Confidential Therapeutic Services<br>in the Heart of Old Town</h1>

    <blockquote class="quote">
      "A big part of letting go is recognising when it is time to stay in a situation and when it is time to move on."
      <span class="quote__author">- Lorna P. Ashby</span>
    </blockquote>

    <section class="therapists">
      <p class="therapists__lead">We have over</p>
      <p class="therapists__body">
        <span class="therapists__highlight">30 carefully selected, qualified and professional therapists</span>
        offering a range of services to help individuals, families and couples.
      </p>
    </section>

    <div class="brand">
      <span class="brand__dot"></span>
      <p class="brand__name">Wellmere Talking<br>Therapies House</p>
    </div>

    <section class="contact">
      <p class="contact__hours">Appointments available<br>throughout the day and evening</p>
      <div class="contact__row">
        <svg class="contact__icon" viewBox="0 0 26 26" aria-hidden="true">
          <rect x="1.5" y="1.5" width="23" height="23" rx="5" fill="none" stroke="#8b8382" stroke-width="1.5"/>
          <path d="M8.5 7.5 l3 -0.5 l1.5 3.5 l-2 1.5 a9 9 0 0 0 4 4 l1.5 -2 l3.5 1.5 l-0.5 3 c-7 0.5 -12 -4.5 -11 -11 z" fill="none" stroke="#8b8382" stroke-width="1.4" stroke-linejoin="round"/>
        </svg>
        <span class="contact__phone">01632 960418</span>
      </div>
      <div class="contact__row">
        <svg class="contact__icon" viewBox="0 0 26 26" aria-hidden="true">
          <path d="M13 24 C7 16 5 13 5 10 a8 8 0 0 1 16 0 c0 3 -2 6 -8 14 z" fill="none" stroke="#8b8382" stroke-width="1.5"/>
          <circle cx="13" cy="10" r="3" fill="none" stroke="#8b8382" stroke-width="1.5"/>
        </svg>
        <span class="contact__text">14 Linden Row, Old Town,<br>Marlow SL7 2QE</span>
      </div>
      <div class="contact__row">
        <svg class="contact__icon" viewBox="0 0 26 26" aria-hidden="true">
          <circle cx="13" cy="13" r="11" fill="none" stroke="#8b8382" stroke-width="1.5"/>
          <ellipse cx="13" cy="13" rx="5" ry="11" fill="none" stroke="#8b8382" stroke-width="1.3"/>
          <path d="M2 13 h22 M4 7.5 h18 M4 18.5 h18" stroke="#8b8382" stroke-width="1.3"/>
        </svg>
        <span class="contact__text">www.wellmere-house.co.uk</span>
      </div>
    </section>
  </article>
</div>
</body>
</html>
```